Sign listing benefits of Wash and Fold Service

Sign 48 inches wide and 24 inches height to showcase service listed above.
Benefits include:
Saves Money
Saves Time
Convenient
Stain Treatment

Looking for something colorful (Blue and white are our business colors) the look of a laundromat business.

```html
<!DOCTYPE html>
<html lang="en">
<head>
<meta charset="utf-8">
<title>Wash and Fold Service – Benefits Sign</title>
<link rel="stylesheet" href="https://fonts.googleapis.com/css2?family=Bebas+Neue&family=Barlow:wght@500&family=Montserrat:wght@600&display=swap">
<style>
  :root {
    --backdrop: #444243;
    --sky-top: #1e80c2;
    --sky-bottom: #7bbbe6;
    --frame: #1249b0;
    --navy: #0d2a66;
    --royal: #0a41b0;
    --icon-deep: #06207a;
    --icon-light: #a8e4ff;
    --white: #ffffff;
  }
  html, body {
    margin: 0;
    width: 1200px;
    height: 1200px;
    overflow: hidden;
    background: var(--backdrop);
  }
  .sign {
    position: absolute;
    left: 50px;
    top: 325px;
    width: 1100px;
    height: 550px;
    background: linear-gradient(to bottom, var(--sky-top), var(--sky-bottom));
    overflow: hidden;
  }
  .sign-frame {
    position: absolute;
    left: 19px;
    top: 23px;
    right: 17px;
    bottom: 11px;
    border: 2px solid var(--frame);
    border-radius: 10px;
  }
  .sign-title {
    position: absolute;
    left: 0;
    top: 0;
    width: 1100px;
    height: 240px;
  }
  .sign-title text {
    font-family: "Montserrat", sans-serif;
    font-weight: 600;
    font-size: 62px;
    fill: var(--white);
    filter: drop-shadow(3px 4px 2px rgba(0, 0, 40, 0.55));
  }
  .benefits-tag {
    position: absolute;
    left: 330px;
    top: 151px;
    width: 440px;
    height: 53px;
    background: var(--navy);
    border-radius: 6px;
    color: var(--white);
    font-family: "Barlow", sans-serif;
    font-weight: 500;
    font-size: 38px;
    letter-spacing: 0.28em;
    line-height: 53px;
    text-align: center;
    text-indent: 0.28em;
  }
  .benefit {
    position: absolute;
    display: flex;
    align-items: center;
    gap: 17px;
  }
  .benefit-icon {
    width: 102px;
    height: 102px;
    flex: none;
  }
  .benefit-label {
    font-family: "Bebas Neue", sans-serif;
    font-size: 74px;
    line-height: 1;
    color: var(--royal);
    -webkit-text-stroke: 4px var(--white);
    paint-order: stroke fill;
    padding-top: 6px;
  }
  .benefit--money { left: 61px; top: 270px; }
  .benefit--time { left: 61px; top: 402px; }
  .benefit--convenient { left: 536px; top: 270px; }
  .benefit--stain { left: 536px; top: 402px; }
</style>
</head>
<body>
  <main class="sign">
    <div class="sign-frame"></div>

    <svg class="sign-title" viewBox="0 0 1100 240" aria-label="Wash and Fold Service">
      <defs>
        <path id="title-arc" d="M 90 190 A 1353 1353 0 0 1 1010 190"/>
        <radialGradient id="badge-fill" cx="40%" cy="35%" r="70%">
          <stop offset="0" stop-color="#0b57c9"/>
          <stop offset="1" stop-color="#061d76"/>
        </radialGradient>
      </defs>
      <text text-anchor="middle"><textPath href="#title-arc" startOffset="50%" textLength="900" lengthAdjust="spacing">WASH AND FOLD SERVICE</textPath></text>
    </svg>

    <div class="benefits-tag">BENEFITS INCLUDE:</div>

    <div class="benefit benefit--money">
      <svg class="benefit-icon" viewBox="0 0 102 102" aria-hidden="true">
        <circle cx="51" cy="51" r="50" fill="none" stroke="#0a3fae" stroke-width="1.5"/>
        <circle cx="51" cy="51" r="46" fill="url(#badge-fill)"/>
        <path d="M28 30 q14 -8 34 -4 l14 -1 v-4 h4 v12 h-4 v-3 q-12 4 -22 2" fill="none" stroke="#dff6ff" stroke-width="4" stroke-linecap="round"/>
        <circle cx="51" cy="49" r="13" fill="#dff6ff"/>
        <text x="51" y="56" text-anchor="middle" font-family="Montserrat, sans-serif" font-weight="600" font-size="19" fill="#0a3fae">$</text>
        <path d="M26 70 v10 h-4 v-12 h4 v3 q10 -3 22 0 l14 -1 q10 -2 16 -8" fill="none" stroke="#dff6ff" stroke-width="4" stroke-linecap="round"/>
      </svg>
      <span class="benefit-label">SAVES MONEY</span>
    </div>

    <div class="benefit benefit--time">
      <svg class="benefit-icon" viewBox="0 0 102 102" aria-hidden="true">
        <circle cx="51" cy="51" r="50" fill="none" stroke="#0a3fae" stroke-width="1.5"/>
        <circle cx="51" cy="51" r="46" fill="url(#badge-fill)"/>
        <circle cx="60" cy="38" r="16" fill="#dff6ff" stroke="#0a3fae" stroke-width="2"/>
        <circle cx="60" cy="38" r="11" fill="none" stroke="#0a3fae" stroke-width="1.5"/>
        <path d="M60 30 v8 l5 4" fill="none" stroke="#0a3fae" stroke-width="2" stroke-linecap="round"/>
        <path d="M22 54 l8 22 q14 6 30 2 l24 -12 q4 -4 -2 -6 l-18 6 q-8 -2 -14 -8 q-8 -6 -16 -4" fill="none" stroke="#dff6ff" stroke-width="4" stroke-linecap="round" stroke-linejoin="round"/>
      </svg>
      <span class="benefit-label">SAVES TIME</span>
    </div>

    <div class="benefit benefit--convenient">
      <svg class="benefit-icon" viewBox="0 0 102 102" aria-hidden="true">
        <circle cx="51" cy="51" r="50" fill="none" stroke="#0a3fae" stroke-width="1.5"/>
        <circle cx="51" cy="51" r="46" fill="url(#badge-fill)"/>
        <path d="M30 66 A 28 28 0 1 1 74 66" fill="none" stroke="var(--icon-light)" stroke-width="9"/>
        <path d="M24 60 l8 14 l10 -10 z" fill="var(--icon-light)"/>
        <path d="M36 50 l12 14 l22 -28" fill="none" stroke="#dff6ff" stroke-width="12" stroke-linecap="round" stroke-linejoin="round"/>
        <path d="M36 50 l12 14 l22 -28" fill="none" stroke="#0a3fae" stroke-width="5" stroke-linecap="round" stroke-linejoin="round"/>
      </svg>
      <span class="benefit-label">CONVENIENT</span>
    </div>

    <div class="benefit benefit--stain">
      <svg class="benefit-icon" viewBox="0 0 102 102" aria-hidden="true">
        <circle cx="51" cy="51" r="50" fill="none" stroke="#0a3fae" stroke-width="1.5"/>
        <circle cx="51" cy="51" r="46" fill="url(#badge-fill)"/>
        <path d="M40 20 q11 8 22 0 l22 10 l-8 16 l-8 -4 v40 h-34 v-40 l-8 4 l-8 -16 z" fill="var(--icon-light)"/>
        <path d="M46 52 q6 -4 10 2 q0 8 -6 12 q-6 -6 -4 -14 z" fill="none" stroke="#0a3fae" stroke-width="2.5"/>
      </svg>
      <span class="benefit-label">STAIN TREATMENT</span>
    </div>
  </main>
</body>
</html>
```